selling natural honey, a sticker showing scenery and creating interest for consumers

i need a design that portrays a natural product and has an energetic feel about it. the product is natural honey from the country. The honey is sourced from the South Burnett region of Queensland and will be sold to stores. The company selling the product is Kestrin Foods. The sticker needs to be energetic and also interesting with a level of sophistication.

Target Market(s)

25-50 mainly females who enjoy natural prducts and willing to pay for good qaulity

Industry/Entity Type

It Company

Requirements
Must have
• a nice scenery background, like hills or open paddocks to portray a country/ natural product.

must have 'Kestrin Foods'

and

'Ridgewell Vale Honey'

included on the sticker
Nice to have
• scenery, maybe a bee or two flying around.
Should not have
• can't have too much of a cartoon look.

needs to be relatively simple and elegant

```html
<!DOCTYPE html>
<html lang="en">
<head>
<meta charset="utf-8">
<title>Kestrin Foods – Ridgewell Vale Honey Sticker</title>
<link rel="stylesheet" href="https://fonts.googleapis.com/css2?family=Mr+Dafoe&display=swap">
<style>
  :root {
    --page-bg: #ffffff;
    --frame-olive: #6b5509;
    --sky-top: #9ea2a5;
    --sky-mid: #c9cccd;
    --sky-low: #eceeed;
    --horizon: #5b8a3c;
    --hill-far: #6f9f3f;
    --hill-mid: #9dcb3c;
    --hill-bright: #b2da4a;
    --hill-near: #7fb42c;
    --hill-deep: #5f9424;
    --sun-glow: #e4f58a;
    --ink: #232323;
  }
  html, body {
    margin: 0;
    padding: 0;
    width: 1200px;
    height: 900px;
    overflow: hidden;
    background: var(--page-bg);
  }
  .sticker-canvas {
    position: relative;
    width: 1200px;
    height: 900px;
  }
  .sticker {
    display: block;
    width: 1200px;
    height: 900px;
  }
  .outer-frame { fill: var(--frame-olive); }
  .inner-ring { fill: none; stroke: var(--frame-olive); stroke-width: 8; }
  .brand-name,
  .product-name {
    font-family: "Mr Dafoe", cursive;
    fill: var(--ink);
  }
  .brand-name { font-size: 96px; letter-spacing: 2px; }
  .product-name { font-size: 64px; letter-spacing: 1px; }
</style>
</head>
<body>
<main class="sticker-canvas">
  <svg class="sticker" viewBox="0 0 1200 900" xmlns="http://www.w3.org/2000/svg">
    <defs>
      <linearGradient id="sceneryGradient" x1="0" y1="0" x2="0" y2="1">
        <stop offset="0" stop-color="var(--sky-top)"/>
        <stop offset="0.14" stop-color="var(--sky-mid)"/>
        <stop offset="0.29" stop-color="var(--sky-low)"/>
        <stop offset="0.33" stop-color="var(--horizon)"/>
        <stop offset="0.42" stop-color="var(--hill-far)"/>
        <stop offset="0.55" stop-color="var(--hill-mid)"/>
        <stop offset="0.66" stop-color="var(--hill-bright)"/>
        <stop offset="0.85" stop-color="var(--hill-near)"/>
        <stop offset="1" stop-color="var(--hill-deep)"/>
      </linearGradient>
      <radialGradient id="sunlitSlope" cx="0.5" cy="0.6" r="0.45">
        <stop offset="0" stop-color="var(--sun-glow)" stop-opacity="0.45"/>
        <stop offset="1" stop-color="var(--sun-glow)" stop-opacity="0"/>
      </radialGradient>
    </defs>

    <ellipse class="outer-frame" cx="619" cy="444" rx="336" ry="426"/>

    <g class="scenery" role="img"
       aria-label="Photograph of rolling green country hills and open paddocks under a cloudy grey sky">
      <ellipse cx="619" cy="445" rx="294" ry="384" fill="url(#sceneryGradient)"/>
      <ellipse cx="619" cy="445" rx="294" ry="384" fill="url(#sunlitSlope)"/>
    </g>

    <ellipse class="inner-ring" cx="618" cy="442" rx="276" ry="348"/>

    <text class="brand-name" x="607" y="328" text-anchor="middle">Kestrin Foods</text>
    <text class="product-name" x="612" y="527" text-anchor="middle">Ridgewell Vale Honey</text>
  </svg>
</main>
</body>
</html>
```